PRK website

Im a Specialty contractor that specializes in fireproofing. Epoxy flooring and terrazo along with poured floors and polished concrete.

We also do fire caulking.

Im the largest specialty flooring healthcare contractor in the south east.

Otto

Contractor

```html
<!DOCTYPE html>
<html lang="en">
<head>
<meta charset="utf-8">
<title>PRK — Specialty Flooring &amp; Fireproofing</title>
<link rel="stylesheet" href="https://fonts.googleapis.com/css2?family=Questrial&display=swap">
<style>
  :root {
    --blue: #0a7bbd;
    --bg: #e6e6e6;
    --page: #f6f6f6;
    --ink: #2b2b2b;
    --text: #444;
    --muted: #8a8a8a;
    --pill: #3a7aa3;
    --line: #c9c9c9;
  }
  * { margin: 0; padding: 0; box-sizing: border-box; }
  html, body { width: 1200px; height: 1002px; overflow: hidden; }
  body {
    position: relative;
    background: var(--bg);
    font-family: "Questrial", "Century Gothic", sans-serif;
    color: var(--text);
  }
  .band { position: absolute; left: 0; width: 1200px; background: var(--blue); }
  .band--top { top: 78px; height: 154px; }
  .band--bottom { top: 698px; height: 304px; }

  .page {
    position: absolute; left: 246px; top: 0; width: 736px; height: 1002px;
    background: repeating-linear-gradient(135deg, #f8f8f8 0 2px, #f2f2f2 2px 3px);
  }

  .abs { position: absolute; }

  .brand { left: 270px; top: 28px; font-size: 22px; color: #111; letter-spacing: 1px; }
  .account { left: 883px; top: 16px; font-size: 9px; color: #222; font-weight: bold; word-spacing: 6px; }
  .social { left: 928px; top: 41px; display: flex; gap: 2px; }
  .social span { width: 14px; height: 14px; border-radius: 2px; background: #4a7bc0; }
  .social span + span { background: #5fb8e6; }

  .nav { left: 108px; top: 94px; width: 138px; list-style: none; }
  .nav li { height: 20px; line-height: 20px; padding-left: 14px; font-size: 13px; color: #fff; }
  .nav li.is-active { background: #fff; color: #222; font-weight: bold; border-radius: 9px 0 0 9px; height: 17px; line-height: 17px; margin-bottom: 3px; }
  .search {
    left: 108px; top: 197px; width: 114px; height: 17px; border-radius: 9px; background: #fff;
    font-size: 10px; color: #999; padding-left: 15px; line-height: 17px;
  }
  .search svg { position: absolute; right: 5px; top: 3px; }

  .hero {
    left: 266px; top: 79px; width: 693px; height: 291px; border-radius: 6px;
    background: linear-gradient(180deg, #d7dfe6 0%, #b9ccd9 35%, #9fb9cc 55%, #3f5f94 75%, #2e4f86 100%);
    box-shadow: 0 8px 8px -4px rgba(0,0,0,.25);
  }
  .dots { left: 888px; top: 358px; display: flex; gap: 4px; }
  .dots span { width: 7px; height: 7px; border-radius: 50%; background: #fff; }
  .dots span:first-child { background: #f39b1f; border: 1px solid #fff; }

  h2 { position: absolute; font-weight: normal; font-size: 17px; color: #222; }
  .about-text {
    left: 266px; top: 431px; width: 465px; font-size: 10.6px; line-height: 12.5px;
    letter-spacing: .35px; word-spacing: 1px;
    text-align: justify; color: var(--text);
  }
  .pill {
    position: absolute; height: 15px; line-height: 15px; padding: 0 5px; border-radius: 8px;
    background: var(--pill); color: #fff; font-size: 9.5px;
  }

  .service { position: absolute; top: 613px; width: 95px; }
  .service .thumb { width: 95px; height: 56px; border-radius: 3px; box-shadow: 0 1px 3px rgba(0,0,0,.3); }
  .service p { font-size: 10px; color: #333; margin-top: 4px; padding-left: 4px; white-space: nowrap; }

  .quote-text { left: 753px; top: 428px; width: 200px; font-size: 10.3px; line-height: 12.5px; color: #444; }
  .field {
    position: absolute; left: 752px; width: 200px; border: 1px solid var(--line); border-radius: 3px;
    background: #fafafa; font-size: 10px; color: #999; padding: 3px 6px; box-shadow: inset 0 1px 2px rgba(0,0,0,.06);
  }
  .btn-browse { text-align: center; background: #ececec; }
  .btn-send {
    position: absolute; left: 752px; top: 654px; width: 200px; height: 20px; border-radius: 3px;
    background: linear-gradient(#4c8bb5, #336f98); color: #fff; font-size: 10px; font-weight: bold;
    text-align: center; line-height: 20px;
  }

  .divider { position: absolute; left: 246px; width: 736px; height: 14px;
    background: radial-gradient(ellipse at 50% 0, rgba(0,0,0,.06), transparent 70%); }

  .news { position: absolute; top: 783px; width: 158px; font-size: 9.8px; line-height: 11.6px; color: #333; }
  .news h3 { font-size: 9.8px; font-weight: bold; color: #333; }

  .footer { left: 246px; top: 946px; width: 736px; text-align: center; font-size: 9.5px; color: var(--muted); }
</style>
</head>
<body>
  <div class="band band--top"></div>
  <div class="band band--bottom"></div>
  <div class="page"></div>

  <header>
    <div class="abs brand">PRK</div>
    <div class="abs account">login | Sign&nbsp;Up</div>
    <div class="abs social" aria-label="Social links"><span></span><span></span></div>
  </header>

  <ul class="abs nav">
    <li class="is-active">Home</li>
    <li>Products</li>
    <li>Services</li>
    <li>About Us</li>
    <li>Contact</li>
  </ul>
  <div class="abs search">search
    <svg width="11" height="11" viewBox="0 0 11 11"><circle cx="5.5" cy="5.5" r="5" fill="#aaa"/><path d="M4.3 3.2 L7.3 5.5 L4.3 7.8 Z" fill="#fff"/></svg>
  </div>

  <div class="abs hero" role="img" aria-label="Bright empty office space with a blue carpeted floor, ceiling lights and windows"></div>
  <div class="abs dots"><span></span><span></span><span></span><span></span><span></span></div>

  <h2 style="left:266px;top:399px;">About Company</h2>
  <p class="abs about-text">This is Pixelsmith's version of Lorem Ipsum. Proin gravida nibh vel velit auctor aliquet. Aenean sollicitudin, lorem quis bibendum auctor, nisi elit consequat ipsum, nec sagittis sem nibh id elit. Duis sed odio sit amet nibh vulputate cursus a sit amet mauris. Morbi accumsan ipsum velit. Nam nec tellus a odio tincidunt auctor a ornare odio. Sed non mauris vitae erat consequat auctor eu in elit. Class aptent taciti sociosqu ad litora torquent per conubia nostra, per inceptos himenaeos. Mauris in erat justo. Nullam ac urna eu felis dapibus condimentum sit amet a augue. Sed non neque elit. Sed ut imperdiet nisi. Proin condimentum fermentum nunc. Etiam pharetra, erat sed fermentum feugiat, velit mauris egestas quam, ut aliquam massa nisl quis neque. Suspendisse in orci enim.</p>
  <span class="pill" style="left:265px;top:551px;">read more</span>

  <h2 style="left:266px;top:583px;">Top Services</h2>
  <div class="service" style="left:266px;">
    <div class="thumb" role="img" aria-label="Floor machine on a polished floor" style="background:linear-gradient(#c9c3b5,#e7e7e2);"></div>
    <p>Fireproofing</p>
  </div>
  <div class="service" style="left:389px;">
    <div class="thumb" role="img" aria-label="Circular industrial ceiling structure" style="background:radial-gradient(circle,#cfd6ec,#5b5f86);"></div>
    <p>Epoxy flooring</p>
  </div>
  <div class="service" style="left:511px;">
    <div class="thumb" role="img" aria-label="Worker spraying a ceiling from a lift" style="background:linear-gradient(#9a9a95,#4b4a47);"></div>
    <p>Terrazo</p>
  </div>
  <div class="service" style="left:634px;">
    <div class="thumb" role="img" aria-label="Machinery on a concrete job site" style="background:linear-gradient(#7d7a72,#2d2b28);"></div>
    <p>Polished concrete</p>
  </div>
  <span class="pill" style="left:264px;top:692px;">more products</span>

  <h2 style="left:753px;top:400px;">Hear from us !</h2>
  <p class="abs quote-text">Get a quick quote for your business and get answered by the us.</p>
  <div class="field" style="top:468px;height:20px;">Name</div>
  <div class="field" style="top:493px;height:20px;">email address</div>
  <div class="field" style="top:518px;height:81px;">message</div>
  <div class="field" style="top:604px;height:20px;">Select Service type</div>
  <div class="field" style="top:629px;height:20px;width:139px;">Upload Files (optional)</div>
  <div class="field btn-browse" style="top:629px;height:20px;left:895px;width:57px;">Browse</div>
  <div class="btn-send">Send</div>

  <div class="divider" style="top:718px;"></div>

  <h2 style="left:265px;top:745px;">Latest News</h2>
  <h2 style="left:618px;top:745px;">Latest Updates</h2>

  <article class="news" style="left:265px;"><h3>Our Company got nominated for Best practice Awards</h3>This is Pixelsmith's version of Lorem Ipsum. Proin gravida nibh vel velit auctor aliquet. Aenean sollicitudin, lorem quis bibendum auctor, nisi elit consequat ipsum, nec sagittis sem nibh id elit.</article>
  <article class="news" style="left:442px;"><h3>Our Company got nominated for Best practice Awards</h3>This is Pixelsmith's version of Lorem Ipsum. Proin gravida nibh vel velit auctor aliquet. Aenean sollicitudin, lorem quis bibendum auctor, nisi elit consequat ipsum, nec sagittis sem nibh id elit.</article>
  <article class="news" style="left:619px;"><h3>Our Company got nominated for Best practice Awards</h3>This is Pixelsmith's version of Lorem Ipsum. Proin gravida nibh vel velit auctor aliquet. Aenean sollicitudin, lorem quis bibendum auctor, nisi elit consequat ipsum, nec sagittis sem nibh id elit.</article>
  <article class="news" style="left:797px;"><h3>Our Company got nominated for Best practice Awards</h3>This is Pixelsmith's version of Lorem Ipsum. Proin gravida nibh vel velit auctor aliquet. Aenean sollicitudin, lorem quis bibendum auctor, nisi elit consequat ipsum, nec sagittis sem nibh id elit.</article>

  <span class="pill" style="left:264px;top:890px;">read more</span>
  <span class="pill" style="left:442px;top:890px;">read more</span>
  <span class="pill" style="left:619px;top:890px;">read more</span>
  <span class="pill" style="left:796px;top:890px;">read more</span>

  <div class="divider" style="top:928px;"></div>
  <footer class="abs footer">@ All rights reserved 2012</footer>
</body>
</html>
```